Mouthguards and Sports Safety

I am trying to make a powerpoint presentation that will be looped as a video in my dental office's waiting room. The point of this is to raise awareness for mouthguards and to inform the viewer that we are making them. The basic text is in the attached presentation, but I need photos and interesting animations to make it appealing

```html
<!DOCTYPE html>
<html lang="en">
<head>
<meta charset="utf-8">
<title>Mouthguards and Sports Safety</title>
<link rel="stylesheet" href="https://fonts.googleapis.com/css2?family=Poppins:wght@400;500;600;700;800&family=Roboto+Slab:wght@600&display=swap">
<style>
:root{
  --page:#eef1f4;
  --orange:#ff3d00;
  --navy:#2d3a55;
  --ink:#262626;
  --white:#ffffff;
  --brown:#7c3b3b;
  --text:#2b2b2b;
}
*{box-sizing:border-box;margin:0;padding:0}
html,body{width:1200px;height:3659px;overflow:hidden;background:var(--page);font-family:"Poppins",sans-serif}
.slide{position:absolute;left:100px;width:1000px;height:563px;overflow:hidden;background:var(--white)}
.abs{position:absolute}
.photo{position:absolute}
.framed{border:9px solid var(--white)}
.page-tab{position:absolute;right:0;bottom:0;width:70px;height:40px;background:var(--orange);clip-path:polygon(30% 0,100% 0,100% 100%,0 100%);color:var(--white);font-size:12px;font-weight:600;display:flex;align-items:center;justify-content:center;padding-left:14px}
.band{position:absolute;inset:0;width:1000px;height:563px}
.heading{color:var(--navy);font-weight:700;font-size:45px;line-height:1.17}
.ticks{list-style:none}
.ticks li{position:relative;padding-left:20px;font-size:12.5px;color:var(--text);line-height:1.6;margin-bottom:14px}
.ticks li svg{position:absolute;left:0;top:4px}

/* cover */
.cover-photo{inset:0;background:linear-gradient(180deg,#6f8f9a 0%,#2d3a33 35%,#1a1f1a 60%,#3f5a34 85%,#2c3d25 100%)}
.cover-title{position:absolute;left:0;right:0;top:228px;text-align:center;color:var(--white);font-weight:800;font-size:46px;line-height:1.15;letter-spacing:.5px}

/* uniform */
.uniform-photo{left:0;top:0;width:1000px;height:283px;background:radial-gradient(ellipse at 50% 30%,#3c4a6b 0%,#1a1f2e 45%,#050608 80%)}
.uniform-title{position:absolute;left:0;right:0;top:60px;text-align:center;color:var(--white);font-weight:700;font-size:45px;line-height:1.2}
.card{position:absolute;top:221px;width:236px;height:260px;color:var(--white);text-align:center;padding:98px 18px 0;font-size:13px;line-height:1.72}
.card.orange{background:var(--orange)}
.card.dark{background:var(--ink)}
.card svg{position:absolute;left:50%;top:28px;transform:translateX(-50%)}

/* contact */
.thanks{background:var(--navy)}
.thanks-title{position:absolute;left:591px;top:118px;color:var(--white);font-weight:800;font-size:42px}
.contact{position:absolute;left:590px;display:flex;gap:14px;color:var(--white)}
.contact .box{width:40px;height:40px;border:2px solid var(--white);display:flex;align-items:center;justify-content:center;flex-shrink:0;margin-top:4px}
.contact h3{font-family:"Roboto Slab",serif;font-weight:600;font-size:21px;line-height:1.3}
.contact p{font-size:16px;line-height:1.6}
</style>
</head>
<body>

<svg width="0" height="0" style="position:absolute">
  <defs>
    <symbol id="tick" viewBox="0 0 12 10"><path d="M1 5.5l3.5 3.5L11 1.5" fill="none" stroke="#ff3d00" stroke-width="2.2" stroke-linecap="round" stroke-linejoin="round"/></symbol>
    <linearGradient id="warm" x1="0" y1="0" x2="1" y2="0"><stop offset="0" stop-color="#7c3b3b"/><stop offset="1" stop-color="#ff3d00"/></linearGradient>
    <linearGradient id="warm-rev" x1="0" y1="0" x2="1" y2="0"><stop offset="0" stop-color="#ff3d00"/><stop offset="1" stop-color="#5a3a4a"/></linearGradient>
    <linearGradient id="cool" x1="0" y1="0" x2="1" y2="0"><stop offset="0" stop-color="#2d3a55"/><stop offset="1" stop-color="#a33a22"/></linearGradient>
  </defs>
</svg>

<!-- Slide 1 -->
<section class="slide" style="top:45px">
  <div class="photo cover-photo" role="img" aria-label="Close-up of a sports net in front of a blurred field and trees"></div>
  <h1 class="cover-title">MOUTHGUARDS AND<br>SPORTS SAFETY</h1>
</section>

<!-- Slide 2 -->
<section class="slide" style="top:648px">
  <div class="photo uniform-photo" role="img" aria-label="Young football player wearing a helmet"></div>
  <h2 class="uniform-title">Make a mouthguard part of<br>your uniform..</h2>
  <div class="card orange" style="left:14px">
    <svg width="68" height="38" viewBox="0 0 68 38" fill="none" stroke="#fff" stroke-width="2"><rect x="3" y="6" width="62" height="26" rx="6"/><path d="M12 6v26M22 6v26M34 6v26M46 6v26M56 6v26M3 19h62"/></svg>
    When it comes to protecting your smile during active sports, a properly fitted mouthguard is a key piece of athletic gear for children and adults
  </div>
  <div class="card dark" style="left:260px">
    <svg width="56" height="56" viewBox="0 0 56 56" fill="none" stroke="#fff" stroke-width="2"><path d="M6 4v24c0 14 10 24 22 24s22-10 22-24V4h-10v24c0 7-5 12-12 12s-12-5-12-12V4z"/><path d="M20 44h16"/></svg>
    Mouthguards typically cover the upper teeth, which are more exposed than the lower teeth
  </div>
  <div class="card orange" style="left:506px">
    <svg width="60" height="60" viewBox="0 0 60 60" fill="none" stroke="#fff" stroke-width="2"><path d="M14 12c-6 0-8 8-6 16 2 7 4 12 5 22 1 6 7 6 8 0l3-12c1-4 5-4 6 0l3 12c1 6 7 6 8 0 1-10 3-15 5-22 2-8-1-16-8-16-4 0-6 2-9 2s-7-2-15-2z"/><path d="M44 6l3-4M50 10l5-2M51 16h5"/></svg>
    Mouthguards cushion impacts that may otherwise cause broken teeth, jaw injuries, or cuts to your lips, tongue, or face.
  </div>
  <div class="card dark" style="left:752px">
    <svg width="60" height="50" viewBox="0 0 60 50" fill="none" stroke="#fff" stroke-width="2"><path d="M4 6h52v10l-6 4v8c0 10-9 18-20 18S10 38 10 28v-8l-6-4z"/><path d="M22 16v16l8 6 8-6V16"/></svg>
    Mouthguards are commonly used in contact sports. However, mouthguards help prevent mouth and jaw injuries even in non contact sports
  </div>
  <div class="page-tab">2</div>
</section>

<!-- Slide 3 -->
<section class="slide" style="top:1243px">
  <svg class="band" viewBox="0 0 1000 563">
    <polygon points="0,0 628,0 0,99" fill="url(#warm)"/>
    <polygon points="0,465 632,563 0,563" fill="url(#cool)"/>
    <rect x="838" y="0" width="162" height="563" fill="#2d3a55"/>
  </svg>
  <div class="photo framed" style="left:542px;top:61px;width:411px;height:444px;background:linear-gradient(135deg,#4b4b4b,#1a1a1a 55%,#6b3a2a)" role="img" aria-label="Boxer with red hand wraps fitting a black mouthguard"></div>
  <h2 class="heading abs" style="left:27px;top:108px">Pick a<br>mouthguard that</h2>
  <ul class="ticks abs" style="left:28px;top:235px;width:470px">
    <li><svg width="12" height="10"><use href="#tick"/></svg>Fits properly and is comfortable</li>
    <li><svg width="12" height="10"><use href="#tick"/></svg>Ideally has been custom made by a dentist</li>
    <li><svg width="12" height="10"><use href="#tick"/></svg>Has enough flex that it won't tear or break, and is thick enough to hold up to a heavy hit</li>
    <li><svg width="12" height="10"><use href="#tick"/></svg>Is easy to clean</li>
    <li><svg width="12" height="10"><use href="#tick"/></svg>Doesn't limit speech or breathing</li>
    <li><svg width="12" height="10"><use href="#tick"/></svg>Stays in place</li>
  </ul>
  <div class="page-tab">3</div>
</section>

<!-- Slide 4 -->
<section class="slide" style="top:1838px">
  <svg class="band" viewBox="0 0 1000 563">
    <rect x="0" y="0" width="165" height="563" fill="#ff3d00"/>
    <polygon points="383,0 1000,0 1000,97" fill="url(#warm)"/>
    <polygon points="1000,455 1000,563 370,563" fill="url(#warm-rev)"/>
  </svg>
  <div class="photo framed" style="left:48px;top:61px;width:411px;height:442px;background:linear-gradient(90deg,#c9ccd0,#eceef0 40%,#d9d4cf 70%,#f4f4f4)" role="img" aria-label="Patient in a dental chair holding her cheek while talking to a dentist"></div>
  <h2 class="heading abs" style="left:501px;top:96px">Tooth<br>Emergencies</h2>
  <h3 class="abs" style="left:501px;top:222px;color:var(--orange);font-weight:600;font-size:19px">Knocked out Permanent Tooth</h3>
  <ul class="ticks abs" style="left:502px;top:264px;width:480px">
    <li><svg width="12" height="10"><use href="#tick"/></svg>Keep the tooth moist – do NOT let it dry out!</li>
    <li><svg width="12" height="10"><use href="#tick"/></svg>Hold it by the crown (the top part that you see)</li>
    <li><svg width="12" height="10"><use href="#tick"/></svg>Rinse the root with lukewarm water. Do NOT scrub the tooth!</li>
    <li><svg width="12" height="10"><use href="#tick"/></svg>Put the tooth gently in its socket</li>
    <li><svg width="12" height="10"><use href="#tick"/></svg>If you can't put it back in the socket, put it in a container with milk</li>
    <li><svg width="12" height="10"><use href="#tick"/></svg>Talk to your dentist as soon as possible – ideally within 15-20 minutes.</li>
  </ul>
  <div class="page-tab">4</div>
</section>

<!-- Slide 5 -->
<section class="slide" style="top:2424px">
  <svg class="band" viewBox="0 0 1000 563">
    <polygon points="0,0 628,0 0,99" fill="url(#warm)"/>
    <polygon points="0,465 632,563 0,563" fill="url(#cool)"/>
    <rect x="838" y="0" width="162" height="563" fill="#262626"/>
  </svg>
  <div class="photo framed" style="left:542px;top:61px;width:411px;height:444px;background:linear-gradient(180deg,#8fd0f0,#bfe3f4 50%,#dfeef4)" role="img" aria-label="Hand placing a clear aligner into a glass of cleaning water"></div>
  <h2 class="heading abs" style="left:27px;top:176px">Do</h2>
  <ul class="ticks abs" style="left:28px;top:240px;width:470px">
    <li><svg width="12" height="10"><use href="#tick"/></svg>Clean your mouthguard after each use with a toothbrush and toothpaste or a denture cleaner. Rinse with cool water after cleaning.</li>
    <li><svg width="12" height="10"><use href="#tick"/></svg>Store in a firm non airtight container.</li>
    <li><svg width="12" height="10"><use href="#tick"/></svg>Check for wear and replace when it no longer fits properly.</li>
    <li><svg width="12" height="10"><use href="#tick"/></svg>Wear your mouthguard during both practice and games.</li>
  </ul>
  <div class="page-tab">5</div>
</section>

<!-- Slide 6 -->
<section class="slide thanks" style="top:3035px">
  <svg class="band" viewBox="0 0 1000 563"><polygon points="0,0 165,0 447,563 0,563" fill="#ff3d00"/></svg>
  <div class="photo framed" style="left:43px;top:65px;width:419px;height:435px;background:linear-gradient(180deg,#8a6a55,#d6a98a 45%,#f1d9a0)" role="img" aria-label="Smiling girl at a dental check-up"></div>
  <h2 class="thanks-title">Thank You!</h2>
  <div class="contact" style="top:195px">
    <div class="box"><svg width="18" height="16" viewBox="0 0 18 16" fill="#fff"><path d="M1 3l5-2 6 2 5-2v12l-5 2-6-2-5 2z"/></svg></div>
    <div><h3>Address</h3><p>Sed ut perspiciatis unde om<br>nis iste natus</p></div>
  </div>
  <div class="contact" style="top:298px">
    <div class="box"><svg width="16" height="16" viewBox="0 0 16 16" fill="#fff"><path d="M4 1l2 4-2 1.5c.8 2 2.5 3.7 4.5 4.5L10 9l4 2-1 3c-6 0-12-6-12-12z"/></svg></div>
    <div><h3>Phone</h3><p>+155-501-4229</p></div>
  </div>
  <div class="contact" style="top:380px">
    <div class="box"><svg width="18" height="14" viewBox="0 0 18 14" fill="#fff"><path d="M1 1h16v12H1z"/><path d="M1 1l8 6 8-6" stroke="#2d3a55" stroke-width="1.6" fill="none"/></svg></div>
    <div><h3>Email</h3><p>info@brightbitedental.com</p></div>
  </div>
</section>

</body>
</html>
```